Sightless Fellowship Hall of San Diego needs an ad/flyer for convention program

Established in 1949, the Sightless Fellowship Hall of San Diego's mission is to enrich the lives of blind and visually impaired adults by preparing them for a normal, active life in a society that is principally sighted by encouraging independence.

Located in Harwick Gardens in San Diego, California, we are a nonprofit that gives blind and visually impaired people in our community an opportunity to socialize and interact. We help members build skills, confidence, and self-esteem through our various social, recreational, and educational activities. We were founded partially by Heron Guild members and receive ongoing funding from them.

We need an 8 1/2 by 11 inch color ad in jpg format. We would like it to be editable. This will be the foundation of our rebranding. The ad will be in a meeting program of the California Herons (californiaherons.example) with the goal of highlighting some of our programs in order to solicit donations from individual Heron Guilds, preferably ongoing ones.

We would like the ad to be generic enough that we can use the ad for other events and as a flyer in the future. We want the ad/flyer to be classic but eye popping with color. We want the design to reflect a professional and lively organization that loves to serve our members. We don’t entirely love our logo, but it’s what we have for now. Our next task will be a new logo design.

We would like to highlight some of our programs for our members include bingo, blind waterskiing and surfing, cooking and ceramic classes, foreign language classes, self defense classes, yoga, and craft classes. Many of the crafts our members make are sold during fundraisers, and they include blankets, scarves, beaded animals, and more. See a sampling of pictures. We provide transportation to and from our Center, free lunch while at the Center, and food to take home. Many of these activities continue during the pandemic via online platforms. We are doing monthly home deliveries of food to our members.

We need donations to keep our programs going, and we have building repairs & maintenance that we need donations in order to complete. See attached document regarding donations. Please reach out if you have questions. Thank you.

Web address: sfhsd.example
Street address: The Sightless Fellowship Hall of San Diego, 2716 Merrow St San Diego, CA 92107
Email address: donation@sfhsd.example
To make a donation: https://sfhsd.example/donate-2/

Donors

NonProfit

Sans Serif

Must have
• Highlight programs and information on how to make a donation.
Nice to have
• Information on how much each dollar donated will go - see attachment
Should not have
• Unprofessional or sloppy details

```html
<!DOCTYPE html>
<html lang="en">
<head>
<meta charset="utf-8">
<title>Sightless Fellowship Hall of San Diego – Donation Flyer</title>
<link href="https://fonts.googleapis.com/css2?family=Libre+Baskerville:wght@700&family=Montserrat:wght@300;400;600;700&display=swap" rel="stylesheet">
<style>
  :root {
    --ink: #1f1f1f;
    --band: #262626;
    --paper: #ffffff;
    --muted: #8a8a8a;
    --soft: #ececec;
    --photo-dark: #3a3a3c;
    --photo-mid: #9a9896;
    --photo-light: #e6e4e2;
  }
  * { box-sizing: border-box; margin: 0; padding: 0; }
  html, body { width: 800px; height: 1200px; overflow: hidden; background: var(--paper); }
  body { font-family: "Montserrat", Arial, sans-serif; color: var(--ink); }
  .flyer { position: relative; width: 800px; height: 1200px; background: var(--paper); overflow: hidden; }

  .hero-photo {
    position: absolute; left: 250px; top: 0; width: 550px; height: 390px;
    background:
      radial-gradient(ellipse 120px 170px at 370px 190px, var(--photo-dark) 0 60%, transparent 100%),
      linear-gradient(180deg, var(--photo-mid) 0%, var(--photo-light) 70%, #cfcdcb 100%);
    -webkit-mask-image: linear-gradient(100deg, transparent 0%, #000 28%);
            mask-image: linear-gradient(100deg, transparent 0%, #000 28%);
  }

  .brand { position: absolute; left: 50px; top: 82px; display: flex; align-items: center; gap: 14px; }
  .brand-mark { width: 22px; height: 22px; background: var(--ink); }
  .brand-name { font-family: "Libre Baskerville", Georgia, serif; font-weight: 700; font-size: 64px; letter-spacing: 2px; color: var(--ink); line-height: 1; }

  .org-title {
    position: absolute; left: 50px; top: 210px;
    font-family: "Libre Baskerville", Georgia, serif; font-weight: 700;
    font-size: 29px; line-height: 1.3; color: var(--ink);
  }

  .section-band {
    position: absolute; left: 0; top: 352px; width: 375px; height: 80px;
    background: var(--band); color: #fff;
    font-family: "Libre Baskerville", Georgia, serif; font-weight: 700;
    font-size: 29px; padding: 20px 0 0 44px;
  }

  .facts { position: absolute; left: 50px; top: 470px; width: 700px; list-style: none; }
  .fact { display: flex; gap: 10px; margin-bottom: 18px; font-size: 10.5px; line-height: 1.4; }
  .fact-num { font-weight: 300; font-size: 17px; color: var(--muted); width: 22px; flex: none; line-height: 1; }
  .fact strong { font-weight: 700; }

  .gallery { position: absolute; left: 50px; top: 700px; display: flex; gap: 8px; }
  .craft-photo { width: 170px; height: 220px; border: 3px solid var(--soft); }
  .craft-blankets { background: linear-gradient(180deg, #8c78b4 0%, #e7a9c1 30%, #6d5f9d 55%, #d7c6e3 75%, #6fc6c0 100%); }
  .craft-angel { background: radial-gradient(ellipse 55px 65px at 85px 150px, #1e3f9a 0 65%, transparent 100%), linear-gradient(180deg, #d8d6d2, #bdb9b3); }

  .fund-box {
    position: absolute; left: 50px; top: 935px; width: 348px; height: 140px;
    background: var(--band); color: #fff; text-align: center;
    font-family: "Libre Baskerville", Georgia, serif; font-weight: 700; font-size: 13.5px; line-height: 1.45;
    padding: 18px 20px 0;
  }
  .fund-box hr { border: 0; border-top: 1px dashed #8a8a8a; margin: 10px 0; }

  .tiers { position: absolute; left: 440px; top: 705px; width: 330px; }
  .tiers-title { font-family: "Libre Baskerville", Georgia, serif; font-weight: 700; font-size: 31px; margin-bottom: 14px; }
  .tier { margin-bottom: 16px; }
  .tier-head { font-family: "Libre Baskerville", Georgia, serif; font-weight: 700; font-size: 17px; margin-bottom: 6px; }
  .tier-head sup { font-size: 10px; }
  .tier-item { display: flex; gap: 6px; font-size: 9.5px; line-height: 1.35; margin-bottom: 5px; }
  .tick { flex: none; width: 9px; height: 9px; margin-top: 1px; }

  .skyline-band {
    position: absolute; left: 0; top: 1075px; width: 800px; height: 125px;
    background: linear-gradient(180deg, var(--paper) 0%, var(--soft) 45%, #f4f4f4 100%);
  }

  .contact { position: absolute; top: 1125px; display: flex; flex-direction: column; gap: 8px; font-size: 12px; line-height: 1.3; }
  .contact-address { left: 50px; width: 240px; }
  .contact-online { left: 320px; }
  .contact-row { display: flex; gap: 8px; align-items: flex-start; }
  .contact-row svg { flex: none; width: 11px; height: 11px; margin-top: 2px; }

  .donate { position: absolute; left: 488px; top: 1118px; display: flex; align-items: center; gap: 14px; }
  .donate-rule { width: 1px; height: 62px; background: var(--ink); position: relative; }
  .donate-rule::after { content: ""; position: absolute; left: 0; top: 24px; border-left: 7px solid var(--ink); border-top: 6px solid transparent; border-bottom: 6px solid transparent; }
  .donate-title { font-family: "Libre Baskerville", Georgia, serif; font-weight: 700; font-size: 21px; text-align: center; }
  .donate-link { display: block; margin-top: 4px; background: var(--band); color: #fff; border-radius: 12px; padding: 3px 18px; font-family: "Libre Baskerville", Georgia, serif; font-weight: 700; font-size: 11.5px; text-align: center; }
</style>
</head>
<body>
<svg width="0" height="0" style="position:absolute">
  <symbol id="tick" viewBox="0 0 10 10"><circle cx="5" cy="5" r="5" fill="#262626"/><path d="M2.6 5.2l1.6 1.6 3.2-3.4" fill="none" stroke="#fff" stroke-width="1.3"/></symbol>
</svg>
<main class="flyer">
  <div class="hero-photo" role="img" aria-label="Photo of a handmade beaded penguin in a Santa hat on a knitted blanket, with a letter board sign behind it"></div>

  <div class="brand"><span class="brand-mark"></span><span class="brand-name">SFH</span></div>
  <h1 class="org-title">The Sightless Fellowship<br>Hall of San Diego</h1>

  <h2 class="section-band">DID YOU KNOW?</h2>

  <ol class="facts">
    <li class="fact"><span class="fact-num">01</span><p>During the pandemic we offer Bingo, Trivia and other virtual games every week, where blind and low vision participants can win SFH bucks. <strong>You can sponsor one day of games for $35.</strong></p></li>
    <li class="fact"><span class="fact-num">02</span><p>You can provide 75 gift bags for our ‘We are in This Together’ home delivery program. Many of our blind and low vision people are isolated and stuck at home. These gift packages are welcomed with enthusiasm and gratefulness. Your rewards are huge smiles and happy faces.</p></li>
    <li class="fact"><span class="fact-num">03</span><p>Our building is over 20 years old and requires ongoing maintenance and repairs</p></li>
    <li class="fact"><span class="fact-num">04</span><p><strong>Fencing (cage) required to protect outside air conditioning units from vandalism. Cost: $2,500</strong></p></li>
    <li class="fact"><span class="fact-num">05</span><p>Wanted: Sponsors for weekly virtual bingo and trivia games: Blind and Low vision participants receive one SFH buck per win. SFH bucks are turned into gift cards and HLT transportation passes. <strong>Sponsor one week for $40. Sponsor 1 month for $160</strong></p></li>
  </ol>

  <div class="gallery">
    <div class="craft-photo craft-blankets" role="img" aria-label="Photo of stacked handmade knitted blankets in purple, pink and teal"></div>
    <div class="craft-photo craft-angel" role="img" aria-label="Photo of a beaded angel ornament with a blue skirt"></div>
  </div>

  <div class="fund-box">
    <p>$1,083 per month or $13,000 per year will fund our entire lunch program for the year.</p>
    <hr>
    <p>Every dollar donated goes to support SFH participants and programs.</p>
  </div>

  <section class="tiers">
    <h2 class="tiers-title">PRE-COVID</h2>
    <div class="tier">
      <h3 class="tier-head"><sup>$</sup>10 per month or <sup>$</sup>120 will buy:</h3>
      <p class="tier-item"><svg class="tick"><use href="#tick"/></svg>60 meals for our lunch program – we serve 130 meals each week</p>
      <p class="tier-item"><svg class="tick"><use href="#tick"/></svg>13 round trip HLT transportation tickets</p>
      <p class="tier-item"><svg class="tick"><use href="#tick"/></svg>Enough beads to make 35 Nora Bell angels in our craft class</p>
    </div>
    <div class="tier">
      <h3 class="tier-head"><sup>$</sup>20 per month or <sup>$</sup>240 will buy:</h3>
      <p class="tier-item"><svg class="tick"><use href="#tick"/></svg>26 round trip HLT transportation tickets</p>
      <p class="tier-item"><svg class="tick"><use href="#tick"/></svg>One month of large print and Braille translation newsletter printing</p>
    </div>
    <div class="tier">
      <h3 class="tier-head"><sup>$</sup>50 per month or <sup>$</sup>600 will buy:</h3>
      <p class="tier-item"><svg class="tick"><use href="#tick"/></svg>300 lunches</p>
      <p class="tier-item"><svg class="tick"><use href="#tick"/></svg>Thanksgiving dinner with all the fixings for 80 to 100 guests</p>
    </div>
    <div class="tier">
      <h3 class="tier-head"><sup>$</sup>100 per month or <sup>$</sup>1200 will buy:</h3>
      <p class="tier-item"><svg class="tick"><use href="#tick"/></svg>Approximately 10 Bingo parties including food and prizes</p>
    </div>
  </section>

  <div class="skyline-band" role="img" aria-label="Faint city skyline silhouette along the bottom edge"></div>

  <address class="contact contact-address" style="font-style:normal">
    <span class="contact-row"><svg viewBox="0 0 10 12"><path d="M5 0a4 4 0 0 0-4 4c0 3 4 8 4 8s4-5 4-8a4 4 0 0 0-4-4zm0 5.5a1.5 1.5 0 1 1 0-3 1.5 1.5 0 0 1 0 3z" fill="#555"/></svg>The Sightless Fellowship Hall of San Diego, 2716 Merrow St San Diego, CA 92107</span>
  </address>
  <div class="contact contact-online">
    <span class="contact-row"><svg viewBox="0 0 12 9"><rect width="12" height="9" rx="1" fill="#555"/><path d="M0.5 0.8L6 5l5.5-4.2" fill="none" stroke="#fff" stroke-width="1"/></svg>donation@sfhsd.example</span>
    <span class="contact-row"><svg viewBox="0 0 12 12"><circle cx="6" cy="6" r="5.3" fill="none" stroke="#555" stroke-width="1.2"/><ellipse cx="6" cy="6" rx="2.4" ry="5.3" fill="none" stroke="#555"/><path d="M0.8 6h10.4" stroke="#555"/></svg>www.sfhsd.example</span>
  </div>

  <div class="donate">
    <span class="donate-rule"></span>
    <div>
      <p class="donate-title">To make a donation</p>
      <span class="donate-link">https://sfhsd.example/donate-2/</span>
    </div>
  </div>
</main>
</body>
</html>
```